banner ad for a very high end interior designer

Our website only gets a small number of hits per day, but it is often people looking to choose designers to interview. We are going to do a Zolvex remarketing campaign to show ads to people who have previously visited our website. The goal is to make sure they remember the quality and sophistication of our work.
The banner should include pictures of our work. You can see this at www.corinnebalastrodesign.com. Perhaps a single image per banner, or a slideshow within the banner?
The goal is to create awareness and to remind the former website visitor of our work. So it is important to include the logo from our website in the banner ad for visual anchoring and recall. As well, the banner graphics should be of a quality that would be used by Osric Tambel or Pavo Lenk or wexley cousins or vorna or Castelmo.
As for a 'call to action', we can offer "See Our Work in Person" or some simpler wording. If the person clicks on the banner, it will take them to a landing page where they can request free tickets to the Larkmont Residence Interiors Pavilion home. We are designing one of the rooms at that open home event.
Size: either 300 x 250. May buy a second at 320 x 100

```html
<!DOCTYPE html>
<html lang="en">
<head>
<meta charset="utf-8">
<title>Corinne Balastro Design – Remarketing Banners</title>
<link href="https://fonts.googleapis.com/css2?family=Archivo+Black&family=Montserrat:wght@500&family=Roboto:wght@400&display=swap" rel="stylesheet">
<style>
  :root {
    --stage: #ece7e0;
    --paper: #fdfbf9;
    --gold: #d8aa1c;
    --gold-light: #f7d348;
    --gold-deep: #c7900e;
    --ink: #0c0c0c;
    --grey: #6d6d6d;
    --photo-cream: #e9e2d6;
    --photo-light: #f6f3ee;
    --photo-blue: #2d4a8a;
    --photo-navy: #1b2a55;
  }
  * { margin: 0; padding: 0; box-sizing: border-box; }
  html, body { width: 1200px; height: 900px; overflow: hidden; background: var(--stage); }
  .canvas { position: relative; width: 1200px; height: 900px; }

  .banner { position: absolute; background: var(--paper); overflow: hidden; }
  .banner--leaderboard { left: 169px; top: 42px; width: 853px; height: 105px; }
  .banner--rectangle { left: 250px; top: 291px; width: 394px; height: 327px; }
  .banner--skyscraper { left: 738px; top: 178px; width: 188px; height: 703px; }

  .brand-name {
    font-family: "Montserrat", sans-serif; font-weight: 500;
    color: var(--grey); letter-spacing: 0.14em; text-transform: uppercase;
    text-align: center; line-height: 1.25;
  }
  .headline { font-family: "Archivo Black", sans-serif; color: var(--ink); line-height: 1.15; text-align: center; }
  .cta-button {
    display: flex; align-items: center; justify-content: center;
    font-family: "Roboto", sans-serif; color: #1a1205; text-transform: uppercase;
    background: linear-gradient(to bottom, var(--gold-light), var(--gold) 55%, var(--gold-deep));
    border-radius: 6px; box-shadow: 0 1px 2px rgba(0,0,0,0.35);
  }
  .site-url { font-family: "Roboto", sans-serif; color: var(--ink); text-align: center; }
  .work-photo { position: absolute; display: block; }

  /* Leaderboard */
  .banner--leaderboard .brand-block { position: absolute; left: 0; top: 0; width: 208px; height: 105px; display: flex; align-items: center; justify-content: center; }
  .banner--leaderboard .brand-name { font-size: 15px; }
  .banner--leaderboard .work-photo { left: 208px; top: 0; }
  .banner--leaderboard .headline { position: absolute; left: 500px; top: 25px; width: 205px; font-size: 24px; }
  .banner--leaderboard .cta-button { position: absolute; left: 710px; top: 33px; width: 134px; height: 38px; font-size: 21px; }
  .banner--leaderboard .site-url { position: absolute; left: 700px; top: 78px; width: 153px; font-size: 11.5px; }

  /* Rectangle */
  .banner--rectangle .brand-block { position: absolute; left: 0; top: 0; width: 100%; height: 75px; display: flex; align-items: center; justify-content: center; border-bottom: 3px solid var(--gold); }
  .banner--rectangle .brand-name { font-size: 17px; }
  .banner--rectangle .work-photo { left: 0; top: 75px; }
  .banner--rectangle .headline { position: absolute; left: 2px; top: 265px; width: 206px; font-size: 23px; }
  .banner--rectangle .cta-button { position: absolute; left: 224px; top: 256px; width: 158px; height: 43px; font-size: 25px; }
  .banner--rectangle .site-url { position: absolute; left: 214px; top: 303px; width: 178px; font-size: 12.5px; }

  /* Skyscraper */
  .banner--skyscraper .brand-block { position: absolute; left: 0; top: 0; width: 100%; height: 123px; display: flex; align-items: center; justify-content: center; border-bottom: 3px solid var(--gold); padding: 0 10px; }
  .banner--skyscraper .brand-name { font-size: 15px; }
  .banner--skyscraper .work-photo { left: 0; top: 123px; }
  .banner--skyscraper .headline { position: absolute; left: 0; top: 400px; width: 100%; font-size: 38px; line-height: 1.28; }
  .banner--skyscraper .cta-button { position: absolute; left: 15px; top: 590px; width: 158px; height: 44px; font-size: 25px; }
  .banner--skyscraper .site-url { position: absolute; left: 0; top: 642px; width: 100%; font-size: 12.5px; }
</style>
</head>
<body>
<main class="canvas">

  <svg width="0" height="0" aria-hidden="true" style="position:absolute">
    <defs>
      <linearGradient id="roomTones" x1="0" y1="0" x2="1" y2="1">
        <stop offset="0" stop-color="var(--photo-cream)"/>
        <stop offset="0.35" stop-color="var(--photo-light)"/>
        <stop offset="0.55" stop-color="var(--photo-blue)"/>
        <stop offset="0.75" stop-color="var(--photo-light)"/>
        <stop offset="1" stop-color="var(--photo-navy)"/>
      </linearGradient>
    </defs>
  </svg>

  <section class="banner banner--leaderboard">
    <div class="brand-block"><span class="brand-name">Corinne Balastro</span></div>
    <svg class="work-photo" width="300" height="105" viewBox="0 0 300 105" role="img" aria-label="Photograph of a bright bedroom with blue curtains, a curved navy sofa and a white bed with a navy throw">
      <polygon points="0,0 290,0 290,62 250,105 0,105" fill="url(#roomTones)"/>
      <polyline points="290,0 290,62 250,105" fill="none" stroke="var(--gold)" stroke-width="3"/>
    </svg>
    <div class="headline">See Our Work<br>in Person</div>
    <div class="cta-button">Click Here</div>
    <div class="site-url">corinnebalastrodesign.com</div>
  </section>

  <section class="banner banner--rectangle">
    <div class="brand-block"><span class="brand-name">Corinne Balastro</span></div>
    <svg class="work-photo" width="394" height="185" viewBox="0 0 394 185" role="img" aria-label="Photograph of a bedroom with fireplace, artwork, blue curtains, a curved navy sofa and a white bed">
      <polygon points="0,0 394,0 394,156 234,156 200,182 0,182" fill="url(#roomTones)"/>
      <polyline points="394,156 234,156 200,182 0,182" fill="none" stroke="var(--gold)" stroke-width="3"/>
    </svg>
    <div class="headline">See Our Work<br>in Person</div>
    <div class="cta-button">Click Here</div>
    <div class="site-url">corinnebalastrodesign.com</div>
  </section>

  <section class="banner banner--skyscraper">
    <div class="brand-block"><span class="brand-name">Corinne Balastro</span></div>
    <svg class="work-photo" width="188" height="258" viewBox="0 0 188 258" role="img" aria-label="Photograph of a bedroom with blue curtains, a navy sofa and a white bed with a navy throw">
      <polygon points="0,0 188,0 188,232 80,232 50,256 0,256" fill="url(#roomTones)"/>
      <polyline points="188,232 80,232 50,256 0,256" fill="none" stroke="var(--gold)" stroke-width="3"/>
    </svg>
    <div class="headline">See Our<br>Work in<br>Person</div>
    <div class="cta-button">Click Here</div>
    <div class="site-url">corinnebalastrodesign.com</div>
  </section>

</main>
</body>
</html>
```